Kelvaro Pools

Luxury pool designer builder brochure

Company name is "Kelvaro"
Tag line is "Pools for the Mind Body & Soul"
Maybe integrate "Luxury Urban Lifestyle"

Target Market(s)

30 to 65 income of 200000.00 plus Affluent, high end life style
Luxury living

Industry/Entity Type

It Company

Font styles to use
Serif

Colors
000000

Requirements
Must have
• NOTE:
• Please remove the "Aquatic environments for the under the logo.
• I want a black background with a very contemporary feel.
• This is a luxury lifestyle product.

```html
<!DOCTYPE html>
<html lang="en">
<head>
<meta charset="utf-8">
<title>Kelvaro Pools – Brochure Flyers</title>
<link rel="stylesheet" href="https://fonts.googleapis.com/css2?family=Didact+Gothic&display=swap">
<style>
  :root {
    --backdrop: #cfcfcf;
    --panel: #242426;
    --band: #2c5461;
    --band-soft: rgba(44, 84, 97, 0.72);
    --accent: #1f86a3;
    --accent-text: #52b9c6;
    --ink-light: #e9eef0;
    --ink-body: #d4d7d8;
  }
  * { margin: 0; padding: 0; box-sizing: border-box; }
  html, body { width: 1200px; height: 816px; overflow: hidden; }
  body {
    background: var(--backdrop);
    font-family: "Didact Gothic", "Century Gothic", sans-serif;
    position: relative;
  }
  .flyer {
    position: absolute;
    width: 512px;
    background: var(--panel);
    overflow: hidden;
    box-shadow: 0 4px 14px rgba(0,0,0,0.25);
  }
  .flyer--lifestyle { left: 66px; top: 51px; height: 663px; }
  .flyer--details { left: 634px; top: 126px; height: 666px; }

  .hero-photo { position: absolute; left: 0; top: 0; width: 512px; height: 291px; }
  .flyer--lifestyle .hero-photo { background: linear-gradient(180deg, #8a7a66 0%, #6b6a5a 35%, #3d7890 62%, #5a8f8a 100%); }
  .flyer--details .hero-photo { background: linear-gradient(180deg, #a39483 0%, #857565 40%, #2f8f94 68%, #52b4b2 100%); }

  .brand-name {
    position: absolute;
    color: #ffffff;
    font-size: 50px;
    letter-spacing: 1px;
    line-height: 1;
    white-space: nowrap;
  }
  .flyer--lifestyle .brand-name { left: 114px; top: 72px; }
  .flyer--details .brand-name { left: 114px; top: 86px; }

  .kicker {
    position: absolute; left: 0; top: 261px; width: 512px; height: 30px;
    background: var(--band-soft);
    color: var(--ink-light);
    font-size: 18px; letter-spacing: 0.5px;
    padding: 7px 0 0 22px;
  }
  .headline-band {
    position: absolute; left: 0; top: 291px; width: 512px; height: 62px;
    background: var(--band);
    color: #ffffff;
    font-size: 32px;
    padding: 11px 0 0 22px;
    white-space: nowrap;
  }
  .intro-title {
    position: absolute; left: 45px; top: 383px; width: 358px;
    text-align: center; color: var(--ink-light); font-size: 17px;
    padding-bottom: 6px; border-bottom: 1px solid var(--accent-text);
  }
  .body-copy {
    color: var(--ink-body);
    font-size: 9.6px; line-height: 11.7px;
    text-align: justify;
  }
  .flyer--lifestyle .body-copy { position: absolute; left: 22px; top: 418px; width: 471px; }

  .thumb { position: absolute; }
  .thumb--a { background: linear-gradient(180deg, #556b5a, #3d6f86 70%, #7a5a7c); }
  .thumb--b { background: linear-gradient(180deg, #7d8a98, #5a5048 55%, #3f7f95); }
  .thumb--c { background: linear-gradient(180deg, #6c7a88, #8a6b5a 55%, #c9c0b0); }
  .thumb--d { background: linear-gradient(180deg, #9a8a76, #4a9db1 60%, #8f8878); }
  .thumb--e { background: linear-gradient(180deg, #dce4ea, #70777a 50%, #2f7fb0); }
  .thumb--f { background: linear-gradient(180deg, #a8b0a6, #5a6a5a 45%, #3fa2b8); }
  .thumb--g { background: linear-gradient(180deg, #c98b55, #3c4a4a 50%, #2c5fa0); }

  .section-title {
    position: absolute; left: 22px; top: 394px; width: 190px;
    color: var(--accent-text); font-size: 17px; line-height: 18px;
  }
  .details-copy { position: absolute; left: 22px; width: 175px; }
  .details-copy--one { top: 437px; }
  .details-copy--two { top: 541px; }

  .contact-line {
    position: absolute; left: 0; width: 512px;
    text-align: center; color: var(--accent-text); font-size: 12px;
    white-space: nowrap;
  }
  .contact-line .sep { color: var(--ink-body); margin: 0 6px; }
  .flyer--lifestyle .contact-line { top: 624px; }
  .flyer--details .contact-line { top: 625px; }

  .base-stripe { position: absolute; left: 0; bottom: 0; width: 512px; height: 9px; background: var(--accent); }
  .flyer--details .base-stripe { height: 11px; }
</style>
</head>
<body>

<article class="flyer flyer--lifestyle">
  <div class="hero-photo" role="img" aria-label="Dusk view of a luxury home with a long blue pool, fire bowls and landscaped terrace"></div>
  <div class="brand-name">Kelvaro</div>
  <div class="kicker">LUXURY URBAN LIFESTYLE</div>
  <h1 class="headline-band">Pools for the Mind Body &amp; Soul</h1>
  <h2 class="intro-title">Your pool is waiting for you to get started</h2>
  <p class="body-copy">Kelvaro Pools and Outdoors are known for their innovation and excellence in swimming pool design and construction, having been recognized by their peers with many awards. Kelvaro have been designing and building custom pools and outdoor living area’s for over 15 years and has built a reputation for excellence in custom luxury swimming pool design / outdoor living space, planning and construction. As a premium choice Houston pool builder and designer, many of the preeminent homes in the Houston area feature our pools and outdoor living spaces.</p>
  <div class="thumb thumb--a" style="left:26px;top:513px;width:138px;height:92px" role="img" aria-label="Lit garden pool with palms and fire features at night"></div>
  <div class="thumb thumb--b" style="left:190px;top:513px;width:139px;height:92px" role="img" aria-label="Stone pool edge with fire bowl beside a lit house"></div>
  <div class="thumb thumb--c" style="left:354px;top:513px;width:139px;height:92px" role="img" aria-label="Raised pool terrace in front of a single-storey home at dusk"></div>
  <p class="contact-line">design@kelvaroinc.com<span class="sep">|</span>(555) 014-2291<span class="sep">|</span>www.kelvaropools.com</p>
  <div class="base-stripe"></div>
</article>

<article class="flyer flyer--details">
  <div class="hero-photo" role="img" aria-label="Courtyard pool with wide steps, arched loggia and stone water wall"></div>
  <div class="brand-name">Kelvaro</div>
  <div class="kicker">ATTENTION TO DETAILS</div>
  <h1 class="headline-band">Unique Artistic Design Approach</h1>
  <h2 class="section-title">Kelvaro Pools and Outdoors</h2>
  <p class="body-copy details-copy details-copy--one">The company challenges itself to create fresh designs while building durable structures that will last through generations. Because of its construction expertise, Kelvaro Aquatic Environments understands the relative value of materials and their impact on budgets, schedules and quality-of-life issues.</p>
  <p class="body-copy details-copy details-copy--two">“We see ourselves as particularly well-equipped to draw out the best from a site and the materials at hand, thereby balancing imagination with brick-and-mortar reality.</p>
  <div class="thumb thumb--d" style="left:214px;top:402px;width:132px;height:89px" role="img" aria-label="Lakeside pool terrace with fire bowls"></div>
  <div class="thumb thumb--e" style="left:361px;top:402px;width:132px;height:89px" role="img" aria-label="Modern house with pool and cabana"></div>
  <div class="thumb thumb--f" style="left:214px;top:504px;width:132px;height:92px" role="img" aria-label="Pool and spa with umbrella under trees"></div>
  <div class="thumb thumb--g" style="left:361px;top:504px;width:132px;height:92px" role="img" aria-label="Free-form pool lit at sunset"></div>
  <p class="contact-line">design@kelvaroinc.com<span class="sep">|</span>(555) 014-2291<span class="sep">|</span>www.kelvaropools.com</p>
  <div class="base-stripe"></div>
</article>

</body>
</html>
```